LA Billboard Project for Brisk Lending

We are running three different billboards around LA, and we need someone to take the mock-ups I've created and bring this campaign to life. Whatever wording is on the mock-ups should stay the same in the ads you create, but feel free to get creative with layout and style. I've attached our mock-ups, our style guide, our logo, and the necessary specs for the billboards. If you have any questions, feel free to reach out!

```html
<!DOCTYPE html>
<html lang="en">
<head>
<meta charset="utf-8">
<title>Brisk Lending – Mortgage Strategy Billboard</title>
<link rel="stylesheet" href="https://fonts.googleapis.com/css2?family=Poppins:wght@500;600;700;800&display=swap">
<style>
  :root {
    --stage: #4f4f4f;
    --navy-light: #26548d;
    --navy: #1a3f72;
    --navy-deep: #122c55;
    --teal: #3fbfcd;
    --ink: #1b2a52;
    --white: #ffffff;
    --skin-light: #f1d2bd;
    --skin-mid: #e2a88a;
    --skin-shadow: #c98262;
  }
  * { box-sizing: border-box; margin: 0; padding: 0; }
  html, body {
    width: 947px;
    height: 1200px;
    overflow: hidden;
    background: var(--stage);
  }
  .canvas {
    position: relative;
    width: 947px;
    height: 1200px;
    display: flex;
    align-items: center;
  }
  .billboard {
    position: relative;
    width: 947px;
    height: 436px;
    overflow: hidden;
    background:
      radial-gradient(ellipse at 55% 35%, var(--navy-light) 0%, var(--navy) 55%, var(--navy-deep) 100%);
    font-family: "Poppins", sans-serif;
    color: var(--white);
  }
  .footer-band {
    position: absolute;
    left: 0;
    bottom: 0;
    width: 100%;
    height: 49px;
    background: var(--teal);
  }
  .house-frame {
    position: absolute;
    left: 0;
    top: 0;
    width: 947px;
    height: 436px;
  }
  .headline {
    position: absolute;
    left: 0;
    top: 0;
    width: 100%;
    height: 100%;
    text-transform: uppercase;
  }
  .headline__lead {
    position: absolute;
    left: 128px;
    top: 30px;
    font-size: 40px;
    font-weight: 600;
    letter-spacing: 0.5px;
    line-height: 1;
  }
  .headline__main {
    position: absolute;
    left: 124px;
    top: 68px;
    font-size: 122px;
    font-weight: 700;
    letter-spacing: -3px;
    line-height: 1;
  }
  .headline__tail {
    position: absolute;
    left: 457px;
    top: 188px;
    font-size: 64px;
    font-weight: 600;
    letter-spacing: 0;
    line-height: 1;
  }
  .brand-name {
    position: absolute;
    left: 560px;
    top: 292px;
    width: 240px;
    text-align: center;
    font-size: 34px;
    font-weight: 700;
    color: var(--teal);
    line-height: 1;
    letter-spacing: -0.5px;
  }
  .web-address {
    position: absolute;
    right: 144px;
    bottom: 0;
    height: 49px;
    display: flex;
    align-items: center;
    gap: 22px;
    color: var(--ink);
    font-size: 29px;
    font-weight: 800;
    letter-spacing: -0.3px;
  }
  .web-address__icon {
    width: 22px;
    height: 22px;
  }
</style>
</head>
<body>
  <main class="canvas">
    <section class="billboard" aria-label="Brisk Lending mortgage strategy billboard">
      <div class="footer-band"></div>

      <svg class="house-frame" viewBox="0 0 947 436" aria-hidden="false">
        <defs>
          <linearGradient id="hands-photo-tone" x1="0" y1="0" x2="1" y2="1">
            <stop offset="0" stop-color="var(--skin-light)"/>
            <stop offset="0.55" stop-color="var(--skin-mid)"/>
            <stop offset="1" stop-color="var(--skin-shadow)"/>
          </linearGradient>
        </defs>
        <path class="house-frame__photo"
              role="img"
              aria-label="Photo of cupped hands holding a small blue paper house"
              d="M48 444 V352 Q48 332 64 320 L248 196 Q264 186 280 196 L465 320 Q481 332 481 352 V444 Z"
              fill="url(#hands-photo-tone)"
              stroke="var(--teal)"
              stroke-width="12"
              stroke-linejoin="round"/>
      </svg>

      <h1 class="headline">
        <span class="headline__lead">What’s your</span>
        <span class="headline__main">Mortgage</span>
        <span class="headline__tail">Strategy?</span>
      </h1>

      <p class="brand-name">Brisk Lending</p>

      <p class="web-address">
        <svg class="web-address__icon" viewBox="0 0 24 24" aria-hidden="true">
          <g fill="none" stroke="var(--ink)" stroke-width="2.4">
            <circle cx="12" cy="12" r="10"/>
            <ellipse cx="12" cy="12" rx="4.2" ry="10"/>
            <line x1="2" y1="12" x2="22" y2="12"/>
          </g>
        </svg>
        <span>BRISKREFI.COM</span>
      </p>
    </section>
  </main>
</body>
</html>
```